Design some Business Cards for Brightline Paving

I need business cards designed for Brightline Paving. We do concrete, sidewalks, driveways, steps, retaining walls, foundations. Please mention that we do same day estimates. The name on the card should be Gerald Whitcombe. The phone number is (814) 555-0173 no address needs to be listed. We have no logo or graphics currently. So use your creativity.

```html
<!DOCTYPE html>
<html lang="en">
<head>
<meta charset="utf-8">
<title>Brightline Paving – Business Card</title>
<link rel="stylesheet" href="https://fonts.googleapis.com/css2?family=Open+Sans:wght@400;600;700&display=swap">
<style>
  :root {
    --page: #e9e7e3;
    --paper: #f4f5f6;
    --paper-shade: #dcdfe2;
    --slate: #2e353d;
    --slate-deep: #22282f;
    --teal: #2fb7c4;
    --ink: #3a4048;
    --muted: #8a9097;
    --white: #ffffff;
  }
  * { margin: 0; padding: 0; box-sizing: border-box; }
  html, body {
    width: 1200px; height: 1023px; overflow: hidden;
    background: var(--page);
    font-family: "Open Sans", Arial, sans-serif;
  }
  .card {
    position: absolute; left: 120px; top: 237px;
    width: 960px; height: 548px;
    box-shadow: 0 18px 40px rgba(0,0,0,.25);
    overflow: hidden;
  }
  .card-bg { position: absolute; inset: 0; }
  .brand {
    position: absolute; left: 64px; top: 92px;
    display: flex; align-items: center; gap: 20px;
  }
  .brand-mark { width: 46px; height: 46px; background: var(--teal); }
  .brand-name {
    font-size: 56px; font-weight: 700; color: var(--ink);
    letter-spacing: -0.5px; line-height: 1;
  }
  .tagline {
    position: absolute; left: 400px; top: 170px;
    font-size: 17px; color: var(--muted); letter-spacing: 2px;
  }
  .contact { position: absolute; left: 64px; top: 392px; }
  .contact-name {
    font-size: 44px; font-weight: 600; color: var(--teal); line-height: 1.1;
  }
  .contact-phone {
    margin-top: 12px; display: flex; align-items: center; gap: 14px;
    font-size: 30px; color: var(--white);
  }
  .contact-phone svg { width: 26px; height: 26px; }
  .services {
    position: absolute; left: 712px; top: 222px; list-style: none;
    font-size: 25px; line-height: 36px; color: var(--white);
  }
  .services li:nth-child(even) { color: var(--teal); }
</style>
</head>
<body>
  <div class="card">
    <svg class="card-bg" viewBox="0 0 960 548" width="960" height="548" aria-hidden="true">
      <defs>
        <linearGradient id="paperFade" x1="0" y1="0" x2="0" y2="1">
          <stop offset="0" stop-color="#f7f8f9"/>
          <stop offset="1" stop-color="#e2e5e8"/>
        </linearGradient>
        <linearGradient id="slateGloss" x1="0" y1="0" x2="1" y2="1">
          <stop offset="0" stop-color="#3a424b"/>
          <stop offset="0.55" stop-color="#2b3139"/>
          <stop offset="1" stop-color="#22282f"/>
        </linearGradient>
      </defs>
      <rect width="960" height="548" fill="url(#paperFade)"/>
      <polygon points="0,336 960,176 960,548 0,548" fill="url(#slateGloss)"/>
      <line x1="0" y1="326" x2="960" y2="166" stroke="var(--teal)" stroke-width="3"/>
      <line x1="682" y1="218" x2="682" y2="440" stroke="var(--teal)" stroke-width="3"/>
      <line x1="682" y1="440" x2="720" y2="440" stroke="var(--teal)" stroke-width="3"/>
    </svg>

    <div class="brand">
      <span class="brand-mark"></span>
      <span class="brand-name">Brightline Paving</span>
    </div>
    <p class="tagline">Same Day Estimates</p>

    <div class="contact">
      <p class="contact-name">Gerald Whitcombe</p>
      <p class="contact-phone">
        <svg viewBox="0 0 24 24" aria-hidden="true"><path fill="#ffffff" d="M6.6 10.8a15.1 15.1 0 0 0 6.6 6.6l2.2-2.2a1 1 0 0 1 1-.25 11.4 11.4 0 0 0 3.6.57 1 1 0 0 1 1 1V20a1 1 0 0 1-1 1A17 17 0 0 1 3 4a1 1 0 0 1 1-1h3.5a1 1 0 0 1 1 1c0 1.25.2 2.45.57 3.57a1 1 0 0 1-.25 1z"/></svg>
        (814) 555-0173
      </p>
    </div>

    <ul class="services">
      <li>Concrete</li>
      <li>Sidewalks</li>
      <li>Driveways</li>
      <li>Steps</li>
      <li>Retaining Walls</li>
      <li>Foundations</li>
    </ul>
  </div>
</body>
</html>
```